Harold Brisk Mechanical business cards

We need business cards designed for "Harold Brisk Mechanical" "Mechanical & Electrical Contractors" "Specializing in Service & Installation"
"Cooling, Heating, Service, Installations, Residential, Commercial"

```html
<!DOCTYPE html>
<html lang="en">
<head>
<meta charset="utf-8">
<title>Harold Brisk Mechanical — Business Cards</title>
<link rel="stylesheet" href="https://fonts.googleapis.com/css2?family=Exo+2:wght@500;600;700&display=swap">
<style>
  :root {
    --bg: #eceded;
    --card: #ffffff;
    --ink: #1d1a1c;
    --red: #e2001a;
    --white: #ffffff;
    --rule: #3a3a3a;
  }
  * { box-sizing: border-box; margin: 0; padding: 0; }
  html, body { width: 1200px; height: 900px; overflow: hidden; }
  body {
    background: var(--bg);
    font-family: "Exo 2", Arial, sans-serif;
    color: var(--ink);
    position: relative;
  }
  .card {
    position: absolute;
    width: 516px;
    height: 297px;
    background: var(--card);
    box-shadow: 0 1px 3px rgba(0,0,0,0.12);
    overflow: hidden;
  }
  .card--front { left: 71px; top: 137px; }
  .card--back-lined { left: 615px; top: 137px; }
  .card--front-dark { left: 71px; top: 463px; background: var(--ink); }
  .card--back-banded { left: 615px; top: 463px; }

  .brand {
    position: absolute;
    display: flex;
    flex-direction: column;
    align-items: center;
    gap: 14px;
  }
  .brand__square { width: 62px; height: 62px; background: var(--red); }
  .brand__name {
    font-weight: 600;
    font-size: 25px;
    letter-spacing: 0.5px;
    text-transform: uppercase;
    white-space: nowrap;
    color: var(--ink);
  }
  .card--front .brand,
  .card--front-dark .brand { left: 0; right: 0; top: 88px; }
  .card--front-dark .brand__name { color: var(--white); }

  .brand--compact { left: 0; width: 283px; top: 98px; gap: 12px; }
  .brand--compact .brand__square { width: 50px; height: 50px; }
  .brand--compact .brand__name { font-size: 16px; }

  .divider {
    position: absolute;
    left: 273px; top: 47px;
    width: 1px; height: 205px;
    background: var(--rule);
  }

  .contact {
    position: absolute;
    left: 302px;
    top: 64px;
    width: 190px;
    text-transform: uppercase;
  }
  .card--back-banded .contact { left: 299px; top: 60px; }
  .contact__name { font-size: 21px; font-weight: 600; line-height: 1; }
  .contact__title { color: var(--red); font-size: 11.5px; font-weight: 600; margin-top: 4px; }
  .contact__rule { height: 1px; background: var(--rule); width: 173px; margin: 5px 0 8px; }
  .contact__line { font-size: 9.6px; font-weight: 500; line-height: 1.22; }
  .contact__group { margin-top: 10px; }
  .contact__group:first-of-type { margin-top: 10px; }
  .contact__phone {
    color: var(--red);
    font-size: 20px;
    font-weight: 600;
    margin-top: 14px;
    line-height: 1;
    letter-spacing: 0.3px;
  }
  .contact__address {
    font-size: 10.5px;
    font-weight: 600;
    text-transform: none;
    line-height: 1.3;
    margin-top: 4px;
  }
  .card--back-banded .contact__phone { margin-top: 6px; }
  .card--back-banded .contact__group { margin-top: 0; }
  .card--back-banded .contact__group + .contact__group { margin-top: 8px; }

  .band { position: absolute; left: 0; bottom: 0; width: 516px; height: 45px; }
</style>
</head>
<body>

<section class="card card--front">
  <div class="brand">
    <div class="brand__square"></div>
    <div class="brand__name">Harold Brisk Mechanical</div>
  </div>
</section>

<section class="card card--back-lined">
  <div class="brand brand--compact">
    <div class="brand__square"></div>
    <div class="brand__name">Harold Brisk Mechanical</div>
  </div>
  <div class="divider"></div>
  <div class="contact">
    <p class="contact__name">Harold Brisk</p>
    <p class="contact__title">Managing Director</p>
    <div class="contact__group">
      <p class="contact__line">Mechanical &amp; Electrical<br>Contractors</p>
    </div>
    <div class="contact__group">
      <p class="contact__line">Cooling, Heating, Service,<br>Installations,<br>Residential, Commercial</p>
    </div>
    <p class="contact__phone">555-013-4827</p>
    <p class="contact__address">PO Box 5182<br>Millbrook, TX 76099</p>
  </div>
</section>

<section class="card card--front-dark">
  <div class="brand">
    <div class="brand__square"></div>
    <div class="brand__name">Harold Brisk Mechanical</div>
  </div>
</section>

<section class="card card--back-banded">
  <div class="brand brand--compact">
    <div class="brand__square"></div>
    <div class="brand__name">Harold Brisk Mechanical</div>
  </div>
  <div class="contact">
    <p class="contact__name">Harold Brisk</p>
    <p class="contact__title">Managing Director</p>
    <div class="contact__rule"></div>
    <div class="contact__group">
      <p class="contact__line">Mechanical &amp; Electrical<br>Contractors</p>
    </div>
    <div class="contact__group">
      <p class="contact__line">Cooling, Heating, Service,<br>Installations,<br>Residential, Commercial</p>
    </div>
    <div class="contact__rule"></div>
    <p class="contact__phone">555-013-4827</p>
    <p class="contact__address">PO Box 5182<br>Millbrook, TX 76099</p>
  </div>
  <svg class="band" viewBox="0 0 516 45" aria-hidden="true">
    <polygon points="0,31 433,31 431,45 0,45" fill="var(--ink)"/>
    <polygon points="442,16 516,0 516,45 439,45" fill="var(--red)"/>
  </svg>
</section>

</body>
</html>
```